Stationary for an International Church

We need a design for various stationery items - letters/envelopes, Word/PowerPoint pages, based on
- the MBF Logo
- the primary color "bright turquoise" ("vivid cyan"), hex #08e8de
- the font family: Frutiger 55 Roman
To get an image of our organization, please visit velmarhall.org, recent blog entries at https://www.velmarhall.org/blog or annual reports at Downloads

Target Market(s)

Congregation and business partners of the Chruch

Font styles to use
Other font styles liked:
• requirement: Frutiger 55 Roman

Colors
33b8a4

Requirements
Must have
• simple, modern design, a bit unique

```html
<!DOCTYPE html>
<html lang="en">
<head>
<meta charset="utf-8">
<title>Minato Bible Fellowship – Stationery</title>
<link href="https://fonts.googleapis.com/css2?family=Hind:wght@400;500;600&family=Arimo:wght@400&display=swap" rel="stylesheet">
<style>
  :root {
    --brand: #5bc7c8;
    --backdrop: #aaa8a9;
    --paper: #ffffff;
    --ink: #3a3a3a;
    --ink-soft: #555555;
    --rule: #8a8a8a;
  }
  * { box-sizing: border-box; margin: 0; padding: 0; }
  html, body { width: 1200px; height: 770px; overflow: hidden; }
  body {
    background: var(--backdrop);
    position: relative;
    font-family: "Hind", sans-serif;
    color: var(--ink);
  }
  .sheet {
    position: absolute;
    background: var(--paper);
    box-shadow: 2px 2px 5px rgba(0,0,0,.28);
    overflow: hidden;
  }
  .footer-band {
    position: absolute; left: 0; right: 0; bottom: 0;
    height: 5px; background: var(--brand);
  }
  .footer-mark {
    position: absolute; bottom: 7px;
    font-size: 9px; font-weight: 600; color: var(--brand);
    letter-spacing: .5px; line-height: 1;
  }

  /* brand lockup */
  .lockup { position: absolute; width: 82px; text-align: center; }
  .lockup-name {
    font-size: 5.6px; font-weight: 500; color: var(--brand);
    line-height: 1; letter-spacing: .45px; text-transform: uppercase;
    white-space: nowrap;
  }
  .lockup-rule { height: 1px; background: var(--brand); margin: 4px 0 5px; }
  .lockup-tagline {
    font-size: 5.2px; color: var(--brand); letter-spacing: .5px; line-height: 1;
  }

  /* letterhead */
  .letterhead { left: 95px; top: 63px; width: 456px; height: 643px; }
  .letterhead .lockup { left: 45px; top: 105px; }
  .contact {
    position: absolute; left: 292px; top: 50px;
    border-left: 1px solid var(--rule);
    padding-left: 15px; padding-top: 2px; height: 62px;
    font-size: 7.6px; line-height: 9.6px; color: var(--ink-soft);
    font-style: normal;
  }
  .contact-name { color: var(--brand); font-weight: 600; }
  .contact-address { margin-bottom: 5px; }
  .contact-line { display: flex; align-items: center; gap: 5px; }
  .contact-line svg { width: 6px; height: 6px; fill: var(--brand); flex: none; }

  .letter-body {
    position: absolute; left: 47px; top: 247px; width: 360px;
    font-family: "Arimo", sans-serif; color: var(--ink-soft);
  }
  .salutation { font-size: 9.6px; margin-bottom: 12px; color: var(--ink); }
  .letter-body p.copy {
    font-size: 6.6px; line-height: 10.8px; text-align: justify;
    margin-bottom: 10.8px;
  }
  .closing { font-size: 6.8px; margin-top: 32px; }
  .signature {
    margin-top: 14px; width: 58px; height: 18px;
    background: linear-gradient(90deg, #e4e6e8, #f1f2f3);
  }
  .letterhead .footer-mark { right: 32px; }

  /* envelope back */
  .envelope-back { left: 586px; top: 170px; width: 508px; height: 251px; }
  .flap { position: absolute; left: 0; top: 0; width: 508px; height: 81px; }
  .flap-name {
    position: absolute; left: 0; right: 0; top: 38px; text-align: center;
    font-size: 7px; font-weight: 600; color: var(--paper);
    letter-spacing: .6px; text-transform: uppercase;
  }

  /* envelope front */
  .envelope-front { left: 586px; top: 455px; width: 508px; height: 251px; }
  .envelope-front .lockup { left: 27px; top: 84px; }
  .return-address {
    position: absolute; left: 28px; top: 112px;
    font-size: 7.6px; line-height: 9.6px; color: var(--ink-soft);
    font-style: normal;
  }
  .envelope-front .footer-mark { right: 32px; }
</style>
</head>
<body>

  <section class="sheet letterhead">
    <div class="lockup">
      <div class="lockup-name">Minato Bible Fellowship</div>
      <div class="lockup-rule"></div>
      <div class="lockup-tagline">Open doors, one family</div>
    </div>

    <address class="contact">
      <div class="contact-name">Minato Bible Fellowship</div>
      <div class="contact-address">3-2-14 Kaigan, Minato-ku<br>Tokyo 105-0022</div>
      <div class="contact-line">
        <svg viewBox="0 0 10 10" aria-hidden="true"><path d="M2 0.5l2 2-1 1.3c.6 1.3 1.6 2.3 2.9 2.9l1.3-1 2 2-1.4 1.8C4.5 9.3.7 5.5.2 1.9z"/></svg>
        (03) 5550-0182
      </div>
      <div class="contact-line">
        <svg viewBox="0 0 10 10" aria-hidden="true"><path d="M2.5 0h5v3h-5zM0 3.5h10v4H8V6H2v1.5H0zM2.5 6.5h5V10h-5z"/></svg>
        (050) 5550-2741
      </div>
      <div class="contact-line">
        <svg viewBox="0 0 10 10" aria-hidden="true"><path d="M5 0a5 5 0 1 0 0 10A5 5 0 0 0 5 0zm0 1c.6 0 1.3 1.4 1.4 3.5H3.6C3.7 2.4 4.4 1 5 1zM1 5.5h1.6c0 1 .2 2 .5 2.7A4 4 0 0 1 1 5.5zm0-1a4 4 0 0 1 2.1-2.7c-.3.7-.5 1.7-.5 2.7zm4 4.5c-.6 0-1.3-1.4-1.4-3.5h2.8C6.3 7.6 5.6 9 5 9zm1.9-.8c.3-.7.5-1.7.5-2.7H9a4 4 0 0 1-2.1 2.7zM7.4 4.5c0-1-.2-2-.5-2.7A4 4 0 0 1 9 4.5z"/></svg>
        www.velmarhall.org
      </div>
    </address>

    <article class="letter-body">
      <p class="salutation">Dear Mr. Hale,</p>
      <p class="copy">Lorem ipsum dolor sit amet, consectetur adipiscing elit. Donec orci purus, luctus vitae dignissim eu, iaculis sed purus. Vivamus faucibus, ipsum nec aliquet viverra, leo mauris condimentum ligula, sit amet sagittis enim ligula quis arcu. Nam egestas tortor id nisi porttitor mattis. In tortor ante, ultricies in suscipit a, tempus non massa. Vivamus et auctor mi. Fusce vel massa nulla. Phasellus nec eros mauris, et scelerisque orci.</p>
      <p class="copy">Donec malesuada orci vitae nulla accumsan porta a id massa. Quisque accumsan iaculis magna sit amet fringilla. Maecenas consequat, magna eget tincidunt semper, odio nibh rutrum mi, id feugiat ante nisi eu risus. Vestibulum nunc orci, rhoncus a placerat in, ultricies in mi. Cras mattis varius eros, vel fringilla nisi suscipit eget. Quisque scelerisque sagittis nulla at porttitor.</p>
      <p class="copy">Sed id augue vitae urna euismod commodo aliquet a quam. Pellentesque arcu velit, cursus et malesuada ut, consequat et diam. Nullam erat sem, rhoncus id ullamcorper vitae, rhoncus et arcu. In ultricies ultricies nulla, ut rutrum nisi iaculis at. Donec eu magna a metus ornare faucibus. Fusce aliquet faucibus ultricies. Morbi semper, est id tincidunt gravida, sem arcu adipiscing lacus, ac bibendum nulla leo eu purus. Quisque nec diam sed risus consectetur a ccumsan quis quis nibh. Vestibulum id purus lorem.</p>
      <p class="closing">Sincerely,</p>
      <div class="signature" role="img" aria-label="Handwritten signature of the sender"></div>
    </article>

    <div class="footer-mark">MBF</div>
    <div class="footer-band"></div>
  </section>

  <section class="sheet envelope-back">
    <svg class="flap" viewBox="0 0 508 81" aria-hidden="true">
      <path d="M0 0H508L493 45Q483 81 447 81H61Q25 81 15 45Z" fill="var(--brand)"/>
    </svg>
    <div class="flap-name">Minato Bible Fellowship</div>
  </section>

  <section class="sheet envelope-front">
    <div class="lockup">
      <div class="lockup-name">Minato Bible Fellowship</div>
      <div class="lockup-rule"></div>
      <div class="lockup-tagline">Open doors, one family</div>
    </div>
    <address class="return-address">
      <div class="contact-name">Minato Bible Fellowship</div>
      3-2-14 Kaigan, Minato-ku<br>Tokyo 105-0022
    </address>
    <div class="footer-mark">MBF</div>
    <div class="footer-band"></div>
  </section>

</body>
</html>
```